Oral Surgeon Referral Pads

Hello. We need referral pads for Dr Loretta Pembrooke, DDS board certified oral surgeon's new office - Cedar Hollow Oral & Maxillofacial Surgery. See logo uploaded. See some images we would like included
Updates

Designs look the same

Font styles to use
Serif
Script

Colors
00AB8E
00BBA5
67D7C9
C6EFE9
E9F9F6

Requirements
Must have
• Color Pantone 623c. Also foldable business cards

```html
<!DOCTYPE html>
<html lang="en">
<head>
<meta charset="utf-8">
<title>Cedar Hollow Oral &amp; Maxillofacial Surgery – Referral Pad</title>
<link rel="stylesheet" href="https://fonts.googleapis.com/css2?family=Lora:wght@400;500&family=Dancing+Script:wght@500&display=swap">
<style>
  :root {
    --teal: #00ab8e;
    --teal-bright: #00bba5;
    --teal-soft: #67d7c9;
    --teal-pale: #c6efe9;
    --teal-mist: #e9f9f6;
    --ink: #0b5e52;
    --hint: #9cbfb9;
    --paper: #ffffff;
  }
  * { box-sizing: border-box; margin: 0; padding: 0; }
  html, body { width: 848px; height: 1200px; overflow: hidden; background: var(--paper); }
  body { font-family: "Lora", serif; color: var(--ink); }
  .pad { position: relative; width: 848px; height: 1200px; }
  .top-band { position: absolute; left: 0; top: 0; width: 848px; height: 29px; background: var(--teal); }

  .brand { position: absolute; left: 0; width: 848px; text-align: center; font-weight: 500; color: var(--teal); }
  .brand-name { top: 136px; font-size: 38px; letter-spacing: 0.5px; }
  .brand-sub { top: 188px; font-size: 20px; letter-spacing: 0.4px; }

  .panel { position: absolute; left: 44px; width: 759px; border: 1px solid var(--teal); }
  .panel-info { top: 255px; height: 452px; }
  .panel-chart { top: 740px; height: 415px; }
  .tab {
    position: absolute; left: 44px; width: 240px; height: 31px;
    background: var(--teal); color: #fff; border-radius: 0 16px 16px 0;
    font-family: "Dancing Script", cursive; font-weight: 500;
    font-size: 25px; line-height: 31px; padding-left: 14px;
  }
  .tab-info { top: 240px; }
  .tab-chart { top: 725px; }

  .field { position: absolute; font-size: 17px; line-height: 1; transform: translateY(-50%); white-space: nowrap; }
  .hint { color: var(--hint); }
  .rule { position: absolute; left: 69px; height: 2px; background: var(--teal-pale); }
  .rule.full { width: 700px; }
  .rule.short { width: 391px; }

  .radio { position: absolute; display: flex; align-items: center; gap: 8px; font-size: 17px; line-height: 1; transform: translateY(-50%); }
  .radio::before { content: ""; width: 11px; height: 11px; border: 1px solid var(--teal-soft); border-radius: 50%; }

  .chart-title { position: absolute; top: 773px; left: 0; width: 848px; text-align: center; font-size: 17px; }
  .tooth-row { position: absolute; background: var(--teal-mist); border-radius: 6px; }
  .divider { position: absolute; left: 423px; width: 2px; background: var(--teal-pale); }
  .arch-rule { position: absolute; top: 953px; height: 2px; background: var(--teal-pale); }
  .num, .primary { position: absolute; transform: translate(-50%, -50%); font-size: 16px; line-height: 1; }
  .primary { color: var(--teal-bright); }
</style>
</head>
<body>
<main class="pad">
  <div class="top-band"></div>

  <div class="brand brand-name">Cedar Hollow</div>
  <div class="brand brand-sub">Oral &amp; Maxillofacial Surgery</div>

  <section class="panel panel-info"></section>
  <h2 class="tab tab-info">Patient Information</h2>

  <div class="field" style="left:69px;top:314px">Today’s Date</div>
  <div class="field hint" style="left:241px;top:314px">DD</div>
  <div class="field" style="left:283px;top:314px">/</div>
  <div class="field hint" style="left:312px;top:314px">MM</div>
  <div class="field" style="left:368px;top:314px">/</div>
  <div class="field hint" style="left:397px;top:314px">YYYY</div>
  <div class="rule full" style="top:334px"></div>

  <div class="field" style="left:69px;top:357px">Appt. Date</div>
  <div class="field hint" style="left:241px;top:357px">DD</div>
  <div class="field" style="left:283px;top:357px">/</div>
  <div class="field hint" style="left:312px;top:357px">MM</div>
  <div class="field" style="left:368px;top:357px">/</div>
  <div class="field hint" style="left:397px;top:357px">YYYY</div>
  <div class="rule short" style="top:376px"></div>

  <div class="field" style="left:497px;top:357px">Day</div>
  <div class="radio" style="left:549px;top:357px">Mon</div>
  <div class="radio" style="left:620px;top:357px">Tue</div>
  <div class="radio" style="left:691px;top:357px">Wed</div>
  <div class="radio" style="left:549px;top:385px">Thr</div>
  <div class="radio" style="left:620px;top:385px">Fri</div>
  <div class="radio" style="left:691px;top:385px">Sat</div>
  <div class="radio" style="left:549px;top:414px">Sun</div>

  <div class="field" style="left:69px;top:400px">Time</div>
  <div class="field" style="left:241px;top:400px">AM/PM</div>
  <div class="rule short" style="top:420px"></div>

  <div class="field" style="left:69px;top:442px">Patient’s Name</div>
  <div class="rule full" style="top:462px"></div>
  <div class="field" style="left:69px;top:485px">Patient’s Phone Number / Mobile number</div>
  <div class="rule full" style="top:505px"></div>
  <div class="field" style="left:69px;top:528px">Referred by</div>
  <div class="rule full" style="top:548px"></div>
  <div class="field" style="left:69px;top:571px">Additional Comments</div>
  <div class="rule full" style="top:591px"></div>

  <section class="panel panel-chart"></section>
  <h2 class="tab tab-chart">Patient Information</h2>
  <p class="chart-title">Please Mark Teeth or Aread to be Treated</p>

  <div class="tooth-row" role="img" aria-label="Upper right teeth 1 to 8 outline illustrations" style="left:164px;top:828px;width:242px;height:65px"></div>
  <div class="tooth-row" role="img" aria-label="Upper left teeth 9 to 16 outline illustrations" style="left:442px;top:828px;width:241px;height:65px"></div>
  <div class="tooth-row" role="img" aria-label="Lower right teeth 25 to 32 outline illustrations" style="left:164px;top:1006px;width:242px;height:59px"></div>
  <div class="tooth-row" role="img" aria-label="Lower left teeth 17 to 24 outline illustrations" style="left:442px;top:1006px;width:241px;height:59px"></div>

  <div class="divider" style="top:830px;height:108px"></div>
  <div class="divider" style="top:973px;height:106px"></div>
  <div class="arch-rule" style="left:101px;width:304px"></div>
  <div class="arch-rule" style="left:443px;width:304px"></div>

  <span class="num" style="left:179px;top:911px">1</span>
  <span class="num" style="left:218px;top:911px">2</span>
  <span class="num" style="left:259px;top:911px">3</span>
  <span class="num" style="left:296px;top:911px">4</span>
  <span class="num" style="left:324px;top:911px">5</span>
  <span class="num" style="left:348px;top:911px">6</span>
  <span class="num" style="left:375px;top:911px">7</span>
  <span class="num" style="left:400px;top:911px">8</span>
  <span class="num" style="left:451px;top:911px">9</span>
  <span class="num" style="left:474px;top:911px">10</span>
  <span class="num" style="left:498px;top:911px">11</span>
  <span class="num" style="left:526px;top:911px">12</span>
  <span class="num" style="left:555px;top:911px">13</span>
  <span class="num" style="left:589px;top:911px">14</span>
  <span class="num" style="left:628px;top:911px">15</span>
  <span class="num" style="left:666px;top:911px">16</span>

  <span class="primary" style="left:213px;top:936px">A</span>
  <span class="primary" style="left:243px;top:936px">B</span>
  <span class="primary" style="left:272px;top:936px">C</span>
  <span class="primary" style="left:303px;top:936px">D</span>
  <span class="primary" style="left:332px;top:936px">E</span>
  <span class="primary" style="left:513px;top:936px">F</span>
  <span class="primary" style="left:542px;top:936px">G</span>
  <span class="primary" style="left:573px;top:936px">H</span>
  <span class="primary" style="left:599px;top:936px">I</span>
  <span class="primary" style="left:623px;top:936px">J</span>

  <span class="primary" style="left:212px;top:975px">T</span>
  <span class="primary" style="left:239px;top:975px">S</span>
  <span class="primary" style="left:268px;top:975px">R</span>
  <span class="primary" style="left:298px;top:975px">Q</span>
  <span class="primary" style="left:328px;top:975px">P</span>
  <span class="primary" style="left:515px;top:975px">O</span>
  <span class="primary" style="left:546px;top:975px">N</span>
  <span class="primary" style="left:578px;top:975px">M</span>
  <span class="primary" style="left:609px;top:975px">L</span>
  <span class="primary" style="left:637px;top:975px">K</span>

  <span class="num" style="left:175px;top:1081px">32</span>
  <span class="num" style="left:210px;top:1081px">31</span>
  <span class="num" style="left:251px;top:1081px">30</span>
  <span class="num" style="left:285px;top:1081px">29</span>
  <span class="num" style="left:315px;top:1081px">28</span>
  <span class="num" style="left:343px;top:1081px">27</span>
  <span class="num" style="left:372px;top:1081px">26</span>
  <span class="num" style="left:401px;top:1081px">25</span>
  <span class="num" style="left:455px;top:1081px">24</span>
  <span class="num" style="left:481px;top:1081px">23</span>
  <span class="num" style="left:509px;top:1081px">22</span>
  <span class="num" style="left:536px;top:1081px">21</span>
  <span class="num" style="left:563px;top:1081px">20</span>
  <span class="num" style="left:590px;top:1081px">19</span>
  <span class="num" style="left:625px;top:1081px">18</span>
  <span class="num" style="left:673px;top:1081px">17</span>
</main>
</body>
</html>
```